Website for a company offering full serivce charging solutions for electric cars

The company "mero-kant" (english: "mero-edge") offering all-in-one-solutions for charging infrastructure for electric mobility.

There are four products:
1- Wallboxes for single-family homes
2- Solutions for property devloper/-management for property parking space
3- All-in-one-charging solution for municipalities/communities
4- Solutions for tourism/hotels/holiday appartments

The Website structure:
1. Main Page
2.1. Product Page Single Homes
2.2. Product Page Property Management / Parking
2.3. Product Page Municipality
2.4. Product Page Tourism
3. Contact Form / Request for information
4. Imprint / Legal

The Website should be built on Wordpress with a powerful possibility to simply add/modify specific landing pages.

We would like you to implement the website later and also maintain it if possible, but we would be able to do minor modifications by ourselfs (for A/B-Testing)

The website should be clear and simple, easy to understand.
Target group is mainly B2C without deeper knowledge of that topic.

It should suggest, that we will provide a very simple way to get the charging infrastructure done.

We need a contact form, maybe we will use Hubspot later.

Attached you will find a draft of the main page and a landing page (for 2.2) - it is just the content, please ignore the design. We would love to let you create a suitable design.
Also you will find some drafts a bit different for the same story.

I added also a few stock photos, but they don't need to be used! If you have better ideas, you are welcome!

Industry/Entity Type

Charging/Electric mobility

Number of Pages Required

2 page

Font styles to use
Sans Serif

Requirements
Must have
• Based on Wordpress, and the designer should be able to implement it on Wordpress on a later step

```html
<!DOCTYPE html>
<html lang="de">
<head>
<meta charset="utf-8">
<title>mero-kant.de – Ladeinfrastruktur für Elektromobilität</title>
<link href="https://fonts.googleapis.com/css2?family=Audiowide&family=Poppins:wght@400;500;600&display=swap" rel="stylesheet">
<style>
:root{
  --navy:#1b2338;
  --navy-deep:#141a2b;
  --pink:#e6137f;
  --purple:#7a56c6;
  --white:#ffffff;
  --text-light:#e8eaf2;
  --footer-text:#1f2540;
  --grad:linear-gradient(90deg,var(--pink),var(--purple));
}
*{margin:0;padding:0;box-sizing:border-box}
html,body{width:1200px;height:3284px;overflow:hidden}
body{background:var(--navy);font-family:'Poppins',sans-serif;color:var(--white);position:relative}
.abs{position:absolute}
.display{font-family:'Audiowide','Poppins',sans-serif;font-weight:400}

/* header */
.brand{left:160px;top:22px;display:flex;flex-direction:column;align-items:center;gap:6px}
.brand-dot{width:30px;height:30px;border-radius:50%;border:4px solid var(--pink)}
.brand-name{font-size:26px;font-weight:500;color:var(--white);white-space:nowrap}
.nav{left:409px;top:34px;display:flex;align-items:center;gap:32px;font-size:12px;font-weight:600;letter-spacing:.3px}
.nav a{color:var(--white);text-decoration:none;white-space:nowrap}
.nav .nav-cta{background:var(--pink);padding:10px 30px;border-radius:20px}

/* hero */
.hero-photo{left:0;top:0;width:1200px;height:642px;
  background:
   radial-gradient(circle at 850px 250px,#3fb2ff 0,#1c6fd6 90px,rgba(30,60,120,0) 260px),
   linear-gradient(90deg,#1d2233 0%,#3a3f52 35%,#51596e 60%,#2a3a66 100%)}
.hero-shade{left:0;top:0;width:1200px;height:642px;background:linear-gradient(90deg,rgba(20,24,40,.75) 0%,rgba(20,24,40,.3) 55%,rgba(20,24,40,0) 100%)}
.hero-intro{left:162px;top:212px;font-size:19px;font-weight:400}
.hero-title{left:160px;top:246px;font-size:47px;line-height:56px;white-space:nowrap}
.btn{display:inline-flex;align-items:center;justify-content:center;border-radius:24px;color:var(--white);font-weight:600;text-decoration:none;white-space:nowrap}
.hero-cta{left:162px;top:376px;width:244px;height:45px;background:var(--pink);font-size:13px;font-family:'Audiowide','Poppins',sans-serif;font-weight:400}
.hero-curve{left:0;top:470px}
.scroll-down{left:567px;top:563px;width:64px;height:64px;border-radius:50%;background:#d9dbe2;display:flex;align-items:center;justify-content:center}
.scroll-down span{width:44px;height:44px;border-radius:50%;background:var(--white);display:flex;align-items:center;justify-content:center}

/* photo placeholders */
.photo{position:absolute;-webkit-mask-image:radial-gradient(ellipse at center,#000 45%,transparent 72%);mask-image:radial-gradient(ellipse at center,#000 45%,transparent 72%)}
.photo-partner{left:0;top:644px;width:600px;height:523px;
  background:radial-gradient(ellipse at 55% 45%,#8a6a3e 0,#4f4a4a 35%,#2b3147 65%,var(--navy) 90%)}
.photo-private{left:560px;top:1300px;width:640px;height:492px;
  background:radial-gradient(ellipse at 70% 45%,#b02a35 0,#5b3447 30%,#2f3a54 58%,var(--navy) 85%)}
.photo-business{left:0;top:1880px;width:650px;height:455px;
  background:radial-gradient(ellipse at 35% 45%,#4a5f86 0,#36476a 35%,#2a3450 60%,var(--navy) 88%)}
.photo-community{left:540px;top:2333px;width:660px;height:460px;
  background:radial-gradient(ellipse at 45% 50%,#d8d9dc 0,#7e7a78 25%,#48506a 55%,var(--navy) 88%)}

/* text blocks */
.h2{font-size:29px;line-height:36px;white-space:nowrap}
.partner-title{left:617px;top:714px}
.partner-copy{left:618px;top:766px;width:420px;font-size:13.4px;line-height:21.7px;letter-spacing:.5px;text-align:justify;color:var(--text-light)}
.partner-copy p+p{margin-top:16px}
.btn-grad{background:var(--grad);font-size:15px;height:36px;width:134px}
.partner-btn{left:618px;top:1049px}
.solutions-title{left:0;top:1190px;width:1200px;text-align:center;font-size:29px;line-height:40px}
.offer-title{font-size:24px;font-weight:500;white-space:nowrap}
.features{list-style:none;font-size:13.3px;line-height:20px;color:var(--text-light)}
.features>li{position:relative;padding-left:30px;margin-bottom:15px}
.features>li svg{position:absolute;left:0;top:2px}
.sub{list-style:none;margin-top:10px;margin-left:-11px}
.sub li{position:relative;padding-left:18px;margin-bottom:5px}
.sub li::before{content:"";position:absolute;left:0;top:8px;width:4px;height:4px;border-radius:50%;background:var(--pink)}
.private-title{left:162px;top:1340px}
.private-list{left:162px;top:1392px;width:400px}
.private-btn{left:162px;top:1688px}
.business-title{left:648px;top:1883px}
.business-list{left:648px;top:1934px;width:400px}
.business-btn{left:646px;top:2268px}
.community-title{left:162px;top:2386px}
.community-list{left:162px;top:2436px;width:440px}
.community-btn{left:162px;top:2722px}

/* footer */
.footer{left:0;top:2869px;width:1200px;height:376px;background:var(--white);color:var(--footer-text)}
.footer h4{font-size:15px;font-weight:600;position:absolute;top:86px}
.quick-links{position:absolute;left:162px;top:118px;list-style:none;font-size:13.5px}
.quick-links li{height:37.5px}
.contact{position:absolute;left:440px;top:126px;font-size:13.5px}
.contact-row{display:flex;gap:12px;align-items:flex-start;margin-bottom:18px}
.contact-icon{width:34px;height:34px;border-radius:50%;background:var(--grad);display:flex;align-items:center;justify-content:center;flex:none}
.contact-row b{font-weight:500;font-size:15px;display:block}
.footer-brand{position:absolute;left:756px;top:86px;width:320px;display:flex;flex-direction:column;align-items:center;gap:4px}
.footer-brand .brand-dot{width:50px;height:50px;border-width:6px}
.footer-brand .brand-name{font-size:40px;line-height:56px;color:var(--footer-text)}
.socials{position:absolute;left:843px;top:231px;display:flex;gap:17px}
.socials span{width:38px;height:38px;border-radius:50%;background:var(--grad)}
.copyright{left:0;top:3245px;width:1200px;height:39px;background:var(--grad);font-size:13px;display:flex;align-items:center;justify-content:center}
</style>
</head>
<body>

<svg width="0" height="0" style="position:absolute">
  <defs>
    <symbol id="plug" viewBox="0 0 18 16">
      <path d="M6 2h4a6 6 0 0 1 0 12H6z" fill="none" stroke="#e6137f" stroke-width="1.6"/>
      <path d="M0 5h6M0 11h6M16 8h2" stroke="#e6137f" stroke-width="1.6"/>
    </symbol>
  </defs>
</svg>

<!-- hero -->
<div class="abs hero-photo" role="img" aria-label="Ladestecker mit blau leuchtendem Ring an einem Elektroauto"></div>
<div class="abs hero-shade"></div>

<header>
  <div class="abs brand"><span class="brand-dot"></span><span class="brand-name">mero-kant.de</span></div>
  <nav class="abs nav">
    <a href="#">einfach mehr als laden</a>
    <a href="#">Lösungen</a>
    <a href="#">Unternehmen</a>
    <a href="#">Services</a>
    <a href="#">Karriere</a>
    <a href="#" class="nav-cta">Kontakt</a>
  </nav>
</header>

<p class="abs hero-intro">Wir bieten Komplettlösungen für die</p>
<h1 class="abs hero-title display">Ladeinfrastruktur<br>für Elektromobilität</h1>
<a href="#" class="abs btn hero-cta">Kontaktieren Sie uns heute</a>

<svg class="abs hero-curve" width="1200" height="175" viewBox="0 0 1200 175">
  <defs>
    <linearGradient id="curveGrad" x1="0" x2="1">
      <stop offset="0" stop-color="#e6137f"/><stop offset="1" stop-color="#7a56c6"/>
    </linearGradient>
  </defs>
  <path d="M0 0 Q600 250 1200 0 V172 H0 Z" fill="url(#curveGrad)"/>
  <path d="M0 30 Q600 250 1200 25 V172 H0 Z" fill="#1b2338"/>
</svg>
<div class="abs scroll-down"><span>
  <svg width="14" height="9" viewBox="0 0 14 9"><path d="M1 1l6 6 6-6" fill="none" stroke="#e6137f" stroke-width="2"/></svg>
</span></div>

<!-- partner -->
<div class="photo photo-partner" role="img" aria-label="Frau lädt ihr Elektroauto und blickt auf ihr Smartphone"></div>
<h2 class="abs h2 display partner-title">Mero-kant Ist Ihr Partner</h2>
<div class="abs partner-copy">
  <p>wenn das Laden nicht nur einfach, sondern die Umsetzung auch aus einer Hand kommen soll Wir bieten Lösungen sowohl für Privatkunden, Geschäfts- kunden als auch Kommunen an, die schnell, fair und ohne Eigenleistung zu einer smarten Ladelösung für E-Fahrzeuge kommen möchten.</p>
  <p>Von der Beratung, über die Installation, Inbetriebnahme bis zur Abrechnung und Wartung bekommen Sie bei mero-kant alles aus einer Hand. Auf Wunsch vermieten wir auch die Ladetechnik und übernehmen im gewerblichen Bereich die direkte Abrechnung mit dem Nutzer.</p>
</div>
<a href="#" class="abs btn btn-grad partner-btn">Alle Ansehen</a>

<h2 class="abs display solutions-title">Fragen Sie Uns Nach Der Auf Ihre Individuellen<br>Bedürfnisse Zugeschnittenen Lösung</h2>

<!-- private -->
<div class="photo photo-private" role="img" aria-label="Frau steckt Ladekabel in ein rotes Elektroauto"></div>
<h3 class="abs offer-title private-title">Als Privatkunde</h3>
<ul class="abs features private-list">
  <li><svg width="18" height="16"><use href="#plug"/></svg>Bestandsanalyse mit umfangreicher Beratung über die Möglichkeiten der Umsetzung</li>
  <li><svg width="18" height="16"><use href="#plug"/></svg>Prüfung und Übernahme der Anmeldung verfügbarer Fördermöglichkeiten</li>
  <li><svg width="18" height="16"><use href="#plug"/></svg>Auswahl an smarten Wallbox Lösungen, passend für Ihr Fahrzeug und Ihre Bedürfnisse</li>
  <li><svg width="18" height="16"><use href="#plug"/></svg>Installation inkl. aller notwendigen Materialien und Tätigkeiten (Durchbrüche, Erdarbeiten, etc.)</li>
  <li><svg width="18" height="16"><use href="#plug"/></svg>Inbetriebnahme und Einweisung in die Ladetechnik</li>
  <li><svg width="18" height="16"><use href="#plug"/></svg>Jährlich technische Wartung nach DGUV3</li>
</ul>
<a href="#" class="abs btn btn-grad private-btn">Alle Ansehen</a>

<!-- business -->
<div class="photo photo-business" role="img" aria-label="Blaues Elektroauto mit orangem Ladekabel an einer Ladesäule"></div>
<h3 class="abs offer-title business-title">Als Geschäftskunde</h3>
<ul class="abs features business-list">
  <li><svg width="18" height="16"><use href="#plug"/></svg>Durchführung einer individuellen Bedarfsanalyse inkl. Ermittlung der Anforderungen für:
    <ul class="sub">
      <li>Haus- und Immobilienverwaltungen</li>
      <li>Dienstleistungs- und Handelsunternehmen</li>
      <li>Hotel und Beherbergungsbetriebe</li>
      <li>Parkraum- und Parkhausbetreiber</li>
      <li>Tourismus, Sport- und Freizeiteinrichtungen</li>
    </ul>
  </li>
  <li><svg width="18" height="16"><use href="#plug"/></svg>Planung und Projektierung des Installationsaufwands inkl. Materialverbrauch</li>
  <li><svg width="18" height="16"><use href="#plug"/></svg>Leasing oder Kauf der Hardware</li>
  <li><svg width="18" height="16"><use href="#plug"/></svg>Normgerechte Installation der Ladeinfrastruktur inkl. Durchbruch-, Brandschutz- und Erdarbeiten</li>
</ul>
<a href="#" class="abs btn btn-grad business-btn">Alle Ansehen</a>

<!-- community -->
<div class="photo photo-community" role="img" aria-label="Öffentliche Ladesäule vor einer Reihe geparkter Autos"></div>
<h3 class="abs offer-title display community-title">Als Kommune</h3>
<ul class="abs features community-list">
  <li><svg width="18" height="16"><use href="#plug"/></svg>Konzeptionierung möglicher Ladeinfrastrukturen innerhalb Ihrer Gemeinde</li>
  <li><svg width="18" height="16"><use href="#plug"/></svg>Planung und Projektsteuerung inkl. sämtlicher behördlicher Genehmigungsverfahren und Beantragung von Fördermitteln</li>
  <li><svg width="18" height="16"><use href="#plug"/></svg>Fachgerechte Installation und Inbetriebnahme</li>
  <li><svg width="18" height="16"><use href="#plug"/></svg>Regelmäßige Wartung gemäß Vorschrif</li>
  <li><svg width="18" height="16"><use href="#plug"/></svg>Reparatur und Kundenservice</li>
  <li><svg width="18" height="16"><use href="#plug"/></svg>Direkte Abrechnung mit dem Nutzer</li>
  <li><svg width="18" height="16"><use href="#plug"/></svg>Beteiligung der Gemeinde am Umsatz</li>
</ul>
<a href="#" class="abs btn btn-grad community-btn">Alle Ansehen</a>

<!-- footer -->
<footer class="abs footer">
  <h4 style="left:162px">Schnelle Links</h4>
  <ul class="quick-links">
    <li>AGB</li><li>Datenschutzerklärung</li><li>Impressum</li><li>Kontakt</li><li>Karriere</li><li>FAQs</li>
  </ul>
  <h4 style="left:440px">Kontaktangaben</h4>
  <div class="contact">
    <div class="contact-row"><span class="contact-icon">
      <svg width="12" height="16" viewBox="0 0 12 16"><path d="M6 0a6 6 0 0 0-6 6c0 4.5 6 10 6 10s6-5.5 6-10a6 6 0 0 0-6-6z" fill="#fff"/><circle cx="6" cy="6" r="2.2" fill="#c3308f"/></svg>
    </span><div><b>Ein Kleid</b>12 Gebäude, Straße, Stadt,<br>Bundesland</div></div>
    <div class="contact-row" style="align-items:center"><span class="contact-icon">
      <svg width="14" height="14" viewBox="0 0 24 24"><path d="M6.6 10.8a15 15 0 0 0 6.6 6.6l2.2-2.2a1 1 0 0 1 1-.25 11.4 11.4 0 0 0 3.6.57 1 1 0 0 1 1 1V20a1 1 0 0 1-1 1A17 17 0 0 1 3 4a1 1 0 0 1 1-1h3.5a1 1 0 0 1 1 1c0 1.250.2 2.45.57 3.6a1 1 0 0 1-.25 1z" fill="#fff"/></svg>
    </span><span>123 456 7890 (Zollfrei)</span></div>
    <div class="contact-row" style="align-items:center"><span class="contact-icon">
      <svg width="14" height="11" viewBox="0 0 14 11"><rect width="14" height="11" rx="1.5" fill="#fff"/><path d="M1 1.5l6 4.5 6-4.5" fill="none" stroke="#c3308f" stroke-width="1.3"/></svg>
    </span><span>&nbsp;info@mero-kant.de.com</span></div>
  </div>
  <div class="footer-brand"><span class="brand-dot"></span><span class="brand-name">mero-kant.de</span></div>
  <div class="socials"><span></span><span></span><span></span></div>
</footer>
<div class="abs copyright">Urheberrecht © 2022 mero-kant.de. Alle Rechte vorbehalten.</div>

</body>
</html>
```